Wine bottle labels - front and back - art and text provided

I have a logo (ai file) with our artwork, as well as all necessary text. I just need someone to put it all together and make it look neat, professional, and stylish, like a regular commercial wine bottle should be. This will be used for the front and back labels for our wine bottles for our very small home vineyard, not commercial use. I would like the style to be similar to the Copper Fern Tulare Basin brand with simple colors (grey and silver), and transparent so they can be screen-printed. I need both ai and jpg files. Note: There need to be two versions of each label. One with the date on the front and the ALC percentage on the back to see the complete look. The second version, without these items. This is because we are having all bottles screen printed without this information since we have a very small production, and will be adding small stickers WITH the information during bottling so that we can use the same bottles for years to come. Art file is attached. Front label text in addition to art: Cabernet Sauvignon 55% / Merlot 45% 2018 California. The back label should read: MARBLEWOOD ESTATE Nestled in the heart of the “Amber Crescent” in Cedar Bluffs, CA, the vineyard at Marblewood Estate enjoys a year-round growing season. Nourished by the fertile black clay soil, the vineyard is surrounded by lush French lavender, fragrant roses, numerous fruit trees, and grazing horses. The Hartwell family has been tending the vineyard at Marblewood Estate since 2014. Our blend of 55% Cabernet Sauvignon and 45% Merlot results in a wine that is deep, vibrant, complex, and full of life. Enjoy our wine responsibly. Salut! Produced and bottled by Marblewood Estate, Alderbrook, California. GOVERNMENT WARNING: (1) ACCORDING TO THE SURGEON GENERAL, WOMEN SHOULD NOT DRINK ALCOHOLIC BEVERAGES DURING PREGNANCY BECAUSE OF THE RISK OF BIRTH DEFECTS. (2) CONSUMPTION OF ALCOHOLIC BEVERAGES IMPAIRS YOUR ABILITY TO DRIVE A CAR OR OPERATE MACHINERY, AND MAY CAUSE HEALTH PROBLEMS. CONTAINS SULFITES / 13.9% ALC BY VOL / 750 ML ***Font can be no smaller than 2mm tall, and items in bold must be the entire Government Warning and the "55% Cabernet Sauvignon / 45% Merlot".

Font styles to use
Serif
Script

Colors
cbcbcb

Requirements
Must have
• Transparent image in grey and silver so that the black bottle will show through the image as a background color.
Nice to have
• It would be nice to see the outline of the artwork in silver and everything else in grey. (see sample file of "Copper Fern" below.)

```html
<!DOCTYPE html>
<html lang="en">
<head>
<meta charset="utf-8">
<title>Marblewood Estate – Back Labels</title>
<link rel="stylesheet" href="https://fonts.googleapis.com/css2?family=Tinos&display=swap">
<style>
  :root {
    --bottle: #050505;
    --silver: #d6d6d6;
    --grey: #cbcbcb;
    --rule: #c4c4c4;
  }
  * { margin: 0; padding: 0; box-sizing: border-box; }
  html, body { width: 1200px; height: 1200px; overflow: hidden; background: var(--bottle); }
  .canvas { position: relative; width: 1200px; height: 1200px; font-family: "Tinos", "Times New Roman", serif; color: var(--grey); }
  .label { position: absolute; border: 2px solid var(--rule); border-radius: 14px; }
  .label--dated { left: 90px; top: 254px; width: 480px; height: 664px; }
  .label--plain { left: 622px; top: 253px; width: 483px; height: 667px; }
  .label__title {
    position: absolute; left: 0; right: 0;
    text-align: center; font-size: 37px; font-weight: 400; color: var(--silver); letter-spacing: 0.3px; white-space: nowrap;
  }
  .label--dated .label__title { top: 23px; }
  .label--plain .label__title { top: 22px; }
  .label__panel { position: absolute; border: 2px solid var(--rule); border-radius: 10px; }
  .label--dated .label__panel { left: 22px; top: 90px; width: 436px; height: 557px; }
  .label--plain .label__panel { left: 22px; top: 89px; width: 439px; height: 553px; }
  .copy { position: absolute; font-size: 14px; line-height: 18px; white-space: nowrap; }
  .copy span { display: block; }
  .label--dated .copy { left: 20px; }
  .label--plain .copy { left: 10px; }
  .volume { position: absolute; left: 0; right: 0; text-align: center; font-size: 14px; line-height: 18px; }
</style>
</head>
<body>
<main class="canvas">

  <section class="label label--dated">
    <h1 class="label__title">MARBLEWOOD ESTATE</h1>
    <div class="label__panel">
      <p class="copy story" style="top:25px">
        <span>Nestled in the heart of the “Amber Crescent” in Cedar Bluffs, CA,</span>
        <span>the vineyard at Marblewood Estate enjoys a year-round growing</span>
        <span>season.</span>
        <span>Nourished by the fertile black clay soil, the vineyard is surrounded</span>
        <span>by lush French lavender, fragrant roses, numerous fruit trees, and</span>
        <span>grazing horses. The Hartwell family has been tending the vineyard</span>
        <span>at Marblewood Estate since 2014.</span>
        <span>Our blend of 55% Cabernet Sauvignon and 45% Merlot results in a</span>
        <span>wine that is deep, vibrant, complex, and full of life.</span>
        <span>Enjoy our wine responsibly. Salut!</span>
      </p>
      <p class="copy producer" style="top:239px">Produced and bottled by Marblewood Estate, Alderbrook, California</p>
      <p class="copy warning" style="top:293px">
        <span>GOVERNMENT WARNING:</span>
        <span>(1) ACCORDING TO THE SURGEON GENERAL, WOMEN</span>
        <span>SHOULD NOT DRINK ALCOHOLIC BEVERAGES DURING</span>
        <span>PREGNANCY BECAUSE OF THE RISK OF BIRTH DEFECTS.</span>
        <span>(2) CONSUMPTION OF ALCOHOLIC BEVERAGES IMPAIRS</span>
        <span>YOUR ABILITY TO DRIVE A CAR OR OPERATE MACHIN-</span>
        <span>ERY, AND MAY CAUSE HEALTH PROBLEMS.</span>
        <span>CONTAINS SULFITES.</span>
      </p>
      <p class="volume" style="top:494px">13.9% ALC BY VOL / 750 ML</p>
    </div>
  </section>

  <section class="label label--plain">
    <h1 class="label__title">MARBLEWOOD ESTATE</h1>
    <div class="label__panel">
      <p class="copy story" style="top:34px">
        <span>Nestled in the heart of the “Amber Crescent” in Cedar Bluffs, CA,</span>
        <span>the vineyard at Marblewood Estate enjoys a year-round growing</span>
        <span>season. Nourished by the fertile black clay soil, the vineyard</span>
        <span>is surrounded by lush French lavender, fragrant roses, numerous</span>
        <span>fruit trees, and grazing horses. The Hartwell family has been tending</span>
        <span>the vineyard at Marblewood Estate since 2014. Our blend of 55%</span>
        <span>Cabernet Sauvignon and 45% Merlot results in a wine that is deep,</span>
        <span>vibrant, complex, and full of life. Enjoy our wine responsibly. Salut!</span>
      </p>
      <p class="copy producer" style="top:214px">Produced and bottled by Marblewood Estate, Alderbrook, California</p>
      <p class="copy warning" style="top:268px">
        <span>GOVERNMENT WARNING:</span>
        <span>(1) ACCORDING TO THE SURGEON GENERAL, WOMEN</span>
        <span>SHOULD NOT DRINK ALCOHOLIC BEVERAGES DURING</span>
        <span>PREGNANCY BECAUSE OF THE RISK OF BIRTH DEFECTS.</span>
        <span>(2) CONSUMPTION OF ALCOHOLIC BEVERAGES IMPAIRS</span>
        <span>YOUR ABILITY TO DRIVE A CAR OR OPERATE</span>
        <span>MACHINERY, AND MAY CAUSE HEALTH PROBLEMS.</span>
        <span>CONTAINS SULFITES.</span>
      </p>
      <p class="volume" style="top:476px">13.9% ALC BY VOL / 750 ML</p>
    </div>
  </section>

</main>
</body>
</html>
```